Gardener needs an exciting new flyer design.

I'm a passionate gardener that requires a custom flyer design for a owner operator gardening business. Design will be for a DL flyer. I'm based on the Sunshine coast in Queensland Australia. My target audience is the residential market on the Sunshine coast. Business name is Tollmere Yards. My services are, lawn mowing, weeding, Eco Friendly fertilizing, green waste removal, Mulching, tree and shrub pruning, Full garden makeovers, hedging, pressure cleaning, privacy screening, Timber deck rejuvenation, Planting, Turf preparation and installation, and much more. Free no obligation quotes, reliable and friendly service, great rates. 12 years experience. Web www.tollmereyards.com.au - Phone 0418527036 - Email kip@tollmereyards.com.au I would like the design to portray a friendly and professional approach.

Target Market(s)

Residential

Industry/Entity Type

Gardener

Font styles to use
Serif

Colors
9ccb3b
abd037
3176b5

Requirements
Must have
• my services, my logo, my contact details,

```html
<!DOCTYPE html>
<html lang="en">
<head>
<meta charset="utf-8">
<title>Tollmere Yards – DL Flyer</title>
<link href="https://fonts.googleapis.com/css2?family=Fondamento&family=Alegreya:wght@400;700&family=Didact+Gothic&family=Archivo+Black&display=swap" rel="stylesheet">
<style>
  :root{
    --green-dark:#1f7a2e;
    --green:#3aa83c;
    --green-light:#9ccb3b;
    --lime:#abd037;
    --blue:#3176b5;
    --grey-panel:#efefef;
    --photo-sky:#a9c9e6;
    --photo-lawn:#6fae45;
    --photo-tone:#86b955;
    --text:#3a3a3a;
    --white:#ffffff;
  }
  *{box-sizing:border-box;margin:0;padding:0}
  html,body{width:744px;height:1200px;overflow:hidden;background:#fff}
  .flyer{position:relative;width:744px;height:1200px;overflow:hidden;background:var(--white);font-family:"Didact Gothic",sans-serif;color:var(--text)}

  .hero-art{position:absolute;left:0;top:0;width:744px;height:380px}
  .brand{position:absolute;left:15px;top:66px;width:300px;text-align:center;font-family:"Fondamento",serif;font-size:25px;line-height:30px;color:var(--green-dark)}
  .brand-dot{display:block;width:40px;height:40px;border-radius:50%;background:var(--green);margin:0 auto 8px}

  .headline{position:absolute;left:0;width:760px;top:308px;text-align:center;font-family:"Fondamento",serif;font-weight:400;color:var(--green-dark);font-size:56px;line-height:48px}
  .headline span{display:block}

  .tagline{position:absolute;left:63px;top:413px;width:622px;height:50px;background:var(--white);border-radius:0 0 18px 18px;box-shadow:0 3px 3px rgba(0,0,0,.18);text-align:center;font-family:"Alegreya",serif;color:var(--green-dark);font-size:23px;line-height:21px;padding-top:4px}
  .tagline b{font-weight:700;font-size:18px}

  .thumbs{position:absolute;left:63px;top:476px;display:flex;gap:9px}
  .thumb{width:148px;height:77px;border-radius:14px;border:2px solid #fff;box-shadow:0 2px 4px rgba(0,0,0,.35);background:var(--photo-tone)}

  .services{position:absolute;left:52px;top:580px;width:639px;height:286px;background:var(--grey-panel);border-radius:18px}
  .services h2{text-align:center;font-family:"Archivo Black",sans-serif;font-weight:400;font-size:25px;color:var(--green-dark);margin-top:10px;letter-spacing:.5px}
  .service-list{position:absolute;top:48px;list-style:none;font-size:22px;line-height:32.7px;white-space:nowrap}
  .service-list li{display:flex;align-items:center;gap:6px}
  .service-list li::before{content:"";width:17px;height:9px;border-radius:0 100% 0 100%;background:linear-gradient(90deg,var(--green),var(--lime));transform:rotate(-25deg)}
  .list-left{left:10px}
  .list-right{left:255px}
  .more{position:absolute;right:9px;top:256px;font-size:20px;line-height:22px}

  .promises{position:absolute;left:52px;top:892px;height:96px;display:flex}
  .promise{text-align:center;color:var(--blue);font-size:19px;line-height:17px}
  .promise-quote{width:229px}
  .promise-service{width:246px;border-left:2px solid var(--blue);border-right:2px solid var(--blue)}
  .promise-rates{width:152px}
  .promise svg{display:block;margin:8px auto 8px}

  .grass{position:absolute;left:0;bottom:0;width:744px;height:190px}
  .contact-title{position:absolute;left:0;right:0;top:1003px;text-align:center;color:var(--green-dark);font-size:25px;line-height:30px}
  .pill{position:absolute;height:28px;border-radius:14px;background:var(--green);color:#fff;display:flex;align-items:center;justify-content:center;gap:10px;font-size:23px;white-space:nowrap}
  .pill-phone{left:239px;width:242px;top:1039px;font-size:25px}
  .pill-web{left:150px;width:437px;top:1072px}
  .pill-mail{left:150px;width:437px;top:1105px}
</style>
</head>
<body>
<main class="flyer">
  <svg class="hero-art" viewBox="0 0 744 380">
    <defs>
      <linearGradient id="heroTone" x1="0" y1="0" x2="0" y2="1">
        <stop offset="0" stop-color="#a9c9e6"/>
        <stop offset="1" stop-color="#6fae45"/>
      </linearGradient>
      <linearGradient id="wave" x1="0" y1="0" x2="1" y2="0">
        <stop offset="0" stop-color="#2f8f2f"/>
        <stop offset="1" stop-color="#8bc34a"/>
      </linearGradient>
    </defs>
    <path d="M0 0H744V236C680 240 600 262 500 300C360 345 200 370 0 330Z" fill="url(#heroTone)" role="img" aria-label="Photo of a manicured lawn and trees in front of a large house"/>
    <path d="M0 330C200 370 360 345 500 300C600 262 680 240 744 236V258C690 262 600 285 500 320C360 360 200 380 0 345Z" fill="url(#wave)"/>
    <path d="M0 345C200 380 360 360 500 320C600 285 690 262 744 258V380H0Z" fill="#fff"/>
    <circle cx="165" cy="50" r="165" fill="#fff"/>
    <path d="M0 140A165 165 0 0 0 322 100" fill="none" stroke="var(--blue)" stroke-width="4" transform="translate(0 30)"/>
  </svg>

  <div class="brand"><span class="brand-dot"></span>Tollmere Yards</div>

  <h1 class="headline"><span>We Make Your</span><span>Garden Beautiful</span></h1>

  <p class="tagline">Trusted &amp; Professional Lawn care &amp; Gardening service<br>with <b>12</b> years experience</p>

  <div class="thumbs">
    <div class="thumb" role="img" aria-label="Photo of a lawn mower on grass"></div>
    <div class="thumb" role="img" aria-label="Photo of a mulched tree base"></div>
    <div class="thumb" role="img" aria-label="Photo of hands weeding a lawn"></div>
    <div class="thumb" role="img" aria-label="Photo of rolled turf being laid"></div>
  </div>

  <section class="services">
    <h2>WHAT WE DO</h2>
    <ul class="service-list list-left">
      <li>Lawn Mowing</li><li>Weeding</li><li>Planting</li><li>Hedging</li><li>Mulching</li><li>Pressure Cleaning</li><li>Privacy Screening</li>
    </ul>
    <ul class="service-list list-right">
      <li>Eco Friendly Fertilizing</li><li>Green Waste Removal</li><li>Tree And Shrub Pruning</li><li>Full Garden Makeovers</li><li>Timber Deck Rejuvenation</li><li>Turf Preparation And Installation</li>
    </ul>
    <p class="more">and much more....</p>
  </section>

  <section class="promises">
    <div class="promise promise-quote">
      <svg width="46" height="46" viewBox="0 0 46 46" fill="none" stroke="currentColor" stroke-width="2"><path d="M6 4h34v28l-10 10H6z"/><path d="M30 42V32h10"/><path d="M12 14h22M12 20h22M12 26h14"/></svg>
      Free no obligation<br>quotes
    </div>
    <div class="promise promise-service">
      <svg width="52" height="46" viewBox="0 0 52 46" fill="none" stroke="currentColor" stroke-width="2"><rect x="4" y="20" width="9" height="22"/><path d="M13 22l10-8 4-12c4 0 6 3 5 8l-2 8h14c3 0 4 3 3 5l-4 15c-1 3-2 4-5 4H13"/></svg>
      Reliable and Friendly<br>Service
    </div>
    <div class="promise promise-rates">
      <svg width="50" height="46" viewBox="0 0 50 46" fill="none" stroke="currentColor" stroke-width="2"><circle cx="28" cy="16" r="9"/><path d="M28 10v12M25 13h5M25 19h5"/><path d="M28 2v3M22 3l1 3M34 3l-1 3"/><path d="M2 32h8l8 4h10c2 0 2 4 0 4H18M10 42l8 2h10l18-10c2-2 0-5-3-4l-13 6"/></svg>
      Great Rates
    </div>
  </section>

  <svg class="grass" viewBox="0 0 744 190" preserveAspectRatio="none" role="img" aria-label="Photo of lush green grass along the bottom edge">
    <defs>
      <linearGradient id="grassTone" x1="0" y1="0" x2="0" y2="1">
        <stop offset="0" stop-color="#fff" stop-opacity="0"/>
        <stop offset="1" stop-color="#6fae45"/>
      </linearGradient>
    </defs>
    <rect width="744" height="190" fill="url(#grassTone)"/>
  </svg>

  <p class="contact-title">Contact Us Now!</p>

  <div class="pill pill-phone">
    <svg width="18" height="18" viewBox="0 0 20 20" fill="none" stroke="#fff" stroke-width="1.6"><circle cx="10" cy="10" r="8.5"/><path d="M7 5l1.5 3-1 1c.7 1.5 1.8 2.6 3.3 3.3l1-1 3 1.5-.8 1.6c-3.6.2-7.7-3.9-7.5-7.5z"/></svg>
    0418527036
  </div>
  <div class="pill pill-web">
    <svg width="18" height="18" viewBox="0 0 20 20" fill="none" stroke="#fff" stroke-width="1.4"><circle cx="10" cy="10" r="8.5"/><ellipse cx="10" cy="10" rx="3.5" ry="8.5"/><path d="M1.5 10h17M3 5.5h14M3 14.5h14"/></svg>
    www.tollmereyards.com.au
  </div>
  <div class="pill pill-mail">
    <svg width="20" height="16" viewBox="0 0 20 16" fill="none" stroke="#fff" stroke-width="1.4"><rect x="1" y="1" width="18" height="14"/><path d="M1 1l9 8 9-8M1 15l6-6M19 15l-6-6"/></svg>
    kip@tollmereyards.com.au
  </div>
</main>
</body>
</html>
```